Morvela Aesthetic Doctor

I require an elegant, luxurious looking business card for my aesthetic business. I am a doctor and that will set me aside from competitors. I am planning to provide home and spa based treatments to clients with high expectations. I have attached my logo.

```html
<!DOCTYPE html>
<html lang="en">
<head>
<meta charset="UTF-8">
<title>Morvela Aesthetic Doctor – Business Card</title>
<link rel="stylesheet" href="https://fonts.googleapis.com/css2?family=Poppins:wght@300;400;500&display=swap">
<style>
  :root {
    --backdrop: #2b2c30;
    --card: #1f2326;
    --card-shade: #262b2f;
    --ink: #e9ecee;
    --silver: #cfd4d8;
    --accent: #5cb8e6;
    --accent-soft: #7fc9ee;
  }
  * { box-sizing: border-box; margin: 0; padding: 0; }
  html, body {
    width: 1200px; height: 800px; overflow: hidden;
    background: var(--backdrop);
    font-family: "Poppins", sans-serif;
  }
  .sheet {
    width: 1200px; height: 800px;
    display: flex; align-items: center; justify-content: center; gap: 40px;
  }
  .card {
    position: relative;
    width: 540px; height: 309px;
    background: var(--card);
    border-radius: 4px;
    box-shadow: 0 18px 40px rgba(0,0,0,.45);
    overflow: hidden;
  }
  .card__texture {
    position: absolute; top: 0; right: 0; width: 60%; height: 100%;
    background: radial-gradient(ellipse at 75% 30%, var(--card-shade) 0%, rgba(38,43,47,0) 70%);
  }
  /* front */
  .front__brand {
    position: absolute; inset: 0;
    display: flex; align-items: center; justify-content: center; gap: 18px;
  }
  .front__mark {
    width: 74px; height: 74px; border-radius: 50%;
    border: 2px solid var(--silver);
    flex: none;
  }
  .front__name {
    font-weight: 300; color: var(--silver);
    font-size: 26px; letter-spacing: 3px; text-transform: uppercase; line-height: 1.25;
  }
  /* back */
  .back__content { position: absolute; left: 34px; top: 40px; right: 34px; }
  .back__name { font-size: 25px; font-weight: 500; color: var(--ink); }
  .back__post { font-size: 11px; font-weight: 400; color: var(--accent); margin-left: 4px; }
  .back__diploma { font-size: 13px; color: var(--accent); margin-top: 2px; }
  .back__rule { height: 1px; background: var(--accent); margin: 14px 0 14px; }
  .back__row { display: flex; justify-content: space-between; }
  .contact { list-style: none; }
  .contact li {
    display: flex; align-items: center; gap: 9px;
    font-size: 13px; color: var(--ink); margin-bottom: 5px;
  }
  .contact svg { width: 15px; height: 15px; flex: none; }
  .social { display: flex; gap: 8px; align-items: flex-start; padding-top: 2px; }
  .social span {
    width: 18px; height: 18px; border-radius: 50%; background: var(--accent);
  }
  .services {
    margin-top: 12px; font-size: 12.5px; font-weight: 300; color: var(--ink); line-height: 1.6;
  }
</style>
</head>
<body>
<main class="sheet">

  <section class="card card--front">
    <div class="card__texture" role="img" aria-label="Faint flowing leaf pattern in dark grey"></div>
    <div class="front__brand">
      <span class="front__mark"></span>
      <p class="front__name">Morvela<br>Aesthetic Doctor</p>
    </div>
  </section>

  <section class="card card--back">
    <div class="card__texture" role="img" aria-label="Faint flowing leaf pattern in dark grey"></div>
    <div class="back__content">
      <h1 class="back__name">Dr Elise Varnow<span class="back__post">MRCPCH MD</span></h1>
      <p class="back__diploma">Australasian Diploma of Aesthetic Medicine</p>
      <div class="back__rule"></div>
      <div class="back__row">
        <ul class="contact">
          <li>
            <svg viewBox="0 0 16 16"><circle cx="8" cy="8" r="8" fill="#5cb8e6"/><path d="M5.2 4.2l1.4 1.6-.8 1c.6 1.2 1.5 2.1 2.6 2.6l1-.8 1.6 1.4-.9 1.4C7.6 11.2 4.8 8.4 4 5.1z" fill="#1f2326"/></svg>
            0800 555 014
          </li>
          <li>
            <svg viewBox="0 0 16 16"><circle cx="8" cy="8" r="8" fill="#5cb8e6"/><rect x="4" y="5" width="8" height="6" fill="none" stroke="#1f2326" stroke-width="1.2"/><path d="M4 5l4 3.4L12 5" fill="none" stroke="#1f2326" stroke-width="1.2"/></svg>
            elise@morvela.co.nz
          </li>
          <li>
            <svg viewBox="0 0 16 16"><circle cx="8" cy="8" r="8" fill="#5cb8e6"/><circle cx="8" cy="8" r="4.2" fill="none" stroke="#1f2326" stroke-width="1.1"/><ellipse cx="8" cy="8" rx="1.8" ry="4.2" fill="none" stroke="#1f2326" stroke-width="1"/><path d="M3.8 8h8.4" stroke="#1f2326" stroke-width="1"/></svg>
            www.morvela.co.nz
          </li>
        </ul>
        <div class="social"><span></span><span></span></div>
      </div>
      <p class="services">
        Dermal injectables - Plasma facials - Microneedling<br>
        Skin boosters - Excessive sweating<br>
        Home and Spa Based Treatments
      </p>
    </div>
  </section>

</main>
</body>
</html>
```